Business Card Design

We are a new residential construction company.our team is made up of young highly skilled tradesman of the next generation of carpenters coming through with new skills and ideas.we chose the name meridian as it means strikingly different from the rest as this is what we plan to be and we would like to portray this in our business card.we like Bold lettering as we want to make a statement, also the use of colour would be great as we want to stand out from the usual plain construction cards and logos.
I have attached a logo sketch I did as a rough idea if you can tidy it up or improve on it would be good.
I have also attached the LBP logo please include this on the card small but still legible.
open to any colourschemes ideas.
thanks
(note)please delete the LBP#308617 off from the card details please.
Updates
Industry/Entity Type
Construction
Contact Information for Business Card
MERIDIAN CONSTRUCTION LIMITED
Director:Kai Pereira
Mobile :0217364801
Email:Meridian.Construction@examplemail.test
Address:48 Halvorsen place,Ashgrove park 2071,Auckland
LBP#BP308617
Look and feel
Each slider illustrates characteristics of the customer's brand and the style your logo design should communicate.

```html
<!DOCTYPE html>
<html lang="en">
<head>
<meta charset="utf-8">
<title>Meridian Construction Limited – Business Card</title>
<link href="https://fonts.googleapis.com/css2?family=Arimo:ital,wght@0,400;0,700;1,700&display=swap" rel="stylesheet">
<style>
  :root {
    --card-bg-light: #fbf5f5;
    --card-bg-warm: #f6ebe6;
    --card-edge: #b9b4b6;
    --ink-dark: #4e494c;
    --ink-title: #5a5558;
    --ink-role: #5f5a5d;
    --brand-blue: #2f8ad0;
    --badge-fill: #cfc9cb;
    --band-mobile: #d2cdcf;
    --band-email: #b7b1b4;
    --band-address: #dbd6d8;
  }
  * { margin: 0; padding: 0; box-sizing: border-box; }
  html, body {
    width: 1200px;
    height: 741px;
    overflow: hidden;
    background: #ffffff;
  }
  .business-card {
    position: relative;
    width: 1200px;
    height: 741px;
    border: 2px solid var(--card-edge);
    background:
      radial-gradient(ellipse at 20% 30%, rgba(240, 220, 210, 0.55), transparent 60%),
      radial-gradient(ellipse at 70% 60%, rgba(245, 228, 220, 0.6), transparent 55%),
      linear-gradient(135deg, var(--card-bg-light), var(--card-bg-warm));
    font-family: "Arimo", Arial, sans-serif;
    overflow: hidden;
  }
  .company-title {
    position: absolute;
    top: 56px;
    left: 0;
    width: 100%;
    text-align: center;
    font-size: 45px;
    font-weight: 700;
    font-style: italic;
    letter-spacing: 0.5px;
    color: var(--ink-title);
  }
  .brand-mark {
    position: absolute;
    left: 74px;
    top: 236px;
    display: flex;
    align-items: center;
    gap: 16px;
  }
  .brand-mark__square {
    width: 40px;
    height: 40px;
    background: var(--brand-blue);
  }
  .brand-mark__name {
    font-size: 50px;
    font-weight: 700;
    color: var(--brand-blue);
    letter-spacing: 1px;
  }
  .certification-badge {
    position: absolute;
    left: 1004px;
    top: 210px;
  }
  .person {
    position: absolute;
    left: 0;
    width: 1200px;
    top: 326px;
    text-align: center;
  }
  .person__name {
    font-size: 56px;
    font-weight: 700;
    color: var(--ink-dark);
    line-height: 1;
  }
  .person__role {
    margin-top: 4px;
    font-size: 32px;
    font-weight: 400;
    color: var(--ink-role);
  }
  .contact-band {
    position: absolute;
    left: 0;
    height: 56px;
    display: flex;
    align-items: center;
    padding-left: 30px;
    font-size: 29px;
    font-weight: 700;
    color: var(--ink-dark);
    white-space: nowrap;
  }
  .contact-band--mobile { top: 558px; width: 370px; background: var(--band-mobile); }
  .contact-band--email { top: 614px; width: 744px; background: var(--band-email); }
  .contact-band--address { top: 670px; width: 1200px; background: var(--band-address); }
</style>
</head>
<body>
  <main class="business-card">
    <h1 class="company-title">MERIDIAN CONSTRUCTION LIMITED</h1>

    <div class="brand-mark">
      <span class="brand-mark__square"></span>
      <span class="brand-mark__name">MERIDIAN</span>
    </div>

    <svg class="certification-badge" width="120" height="120" viewBox="0 0 120 120" role="img" aria-label="Certification badge placeholder">
      <circle cx="60" cy="60" r="58" fill="var(--badge-fill)"/>
    </svg>

    <section class="person">
      <p class="person__name">Kai Pereira</p>
      <p class="person__role">Director</p>
    </section>

    <p class="contact-band contact-band--mobile">Mobile : 0217364801</p>
    <p class="contact-band contact-band--email">Email: Meridian.Construction@examplemail.test</p>
    <p class="contact-band contact-band--address">Address: 48 Halvorsen place,Ashgrove park 2071, Auckland</p>
  </main>
</body>
</html>
```